Dunecrest Motocross Club. Sports club.

We are a family orientated Motocross Club in Abu Dhabi. We have 3 motocross tracks, Intermediate Track, Junior rack and E-track. We also have a School(Academy) and maintenance facility that caters for all motorbike services. We have a BBQ area with a 20x70 meter pool after a hot day of riding. We are busy adding a restaurant and bar in the next few weeks. We host 6 Club races in the season as well as the Sandveil Open Championship. Therefore we will need a race calendar as well as race results page. The school have a dedicated school facility with bike rental, bike show room, gear rental and small shop. We have instructors that instruct kids from 4 years old to professional riders.

Target Market(s)

Motocross riders, kids from 4 years

Industry/Entity Type

extreme sports, motorsports motocross

Coding

Coded - Design and coding required

Number of Pages Required

5+ page

Font styles to use
Sans Serif

Colors

Designer to choose colors to be used in the design.

Requirements
Must have
• User Friendly, Easy to update, Calendar , online payment, race results, academy, facilities,
Nice to have
• Just an update it has to have a calendar with sides that shows whats happening on the day. We also need at the top of page the "open hours", " a next event" button, our partners button at the bottom of page a "News Page" "testimonials" with all the necessary links, social medial, address, contact details, etc.
Should not have
• no cartoons or any clipart please just photos

```html
<!DOCTYPE html>
<html lang="en">
<head>
<meta charset="UTF-8">
<title>Dunecrest Motocross Club – Academy</title>
<link href="https://fonts.googleapis.com/css2?family=Montserrat:wght@400;500;600;700&display=swap" rel="stylesheet">
<style>
  :root {
    --ink-dark: #111111;
    --ember: #4a1416;
    --race-red: #d52228;
    --button-top: #c5242a;
    --button-bottom: #8e1216;
    --text-light: #ffffff;
    --text-soft: #f1e9e9;
  }
  * { margin: 0; padding: 0; box-sizing: border-box; }
  html, body { width: 1200px; height: 675px; overflow: hidden; }
  body {
    font-family: "Montserrat", Arial, sans-serif;
    color: var(--text-light);
    background: linear-gradient(90deg, var(--ink-dark) 0%, var(--ink-dark) 41%, var(--ember) 62%, var(--race-red) 100%);
    position: relative;
  }
  .brand {
    position: absolute; left: 87px; top: 36px;
    display: flex; align-items: center; gap: 8px;
    font-weight: 700; font-size: 14px; color: var(--text-light);
    text-transform: uppercase; letter-spacing: 0.3px;
  }
  .brand-mark { width: 14px; height: 14px; background: var(--race-red); }
  .main-nav {
    position: absolute; top: 34px; left: 646px;
    display: flex; gap: 28px;
    font-weight: 700; font-size: 11px; letter-spacing: 0.6px;
  }
  .main-nav a { color: var(--text-light); text-decoration: none; }
  .hero-intro { position: absolute; left: 84px; top: 131px; width: 360px; }
  .hero-title {
    font-weight: 700; font-size: 33px; line-height: 34px; letter-spacing: 0.5px;
    text-transform: uppercase;
  }
  .hero-tagline { margin-top: 9px; font-size: 15.5px; font-weight: 400; }
  .hero-copy {
    margin-top: 23px; margin-left: 3px; width: 335px;
    font-size: 11.5px; line-height: 18.8px; color: var(--text-soft);
  }
  .cta {
    position: absolute; left: 84px; top: 389px;
    width: 157px; height: 40px; border-radius: 20px;
    background: linear-gradient(180deg, var(--button-top), var(--button-bottom));
    color: var(--text-light); font-weight: 700; font-size: 14.5px;
    display: flex; align-items: center; justify-content: center;
    text-decoration: none;
  }
  .rider-photo {
    position: absolute; left: 443px; top: 123px; width: 267px; height: 428px;
    border-radius: 40% 40% 45% 45%;
    background: radial-gradient(ellipse at 50% 45%, #3a4260 0%, #2a2a36 45%, rgba(40,30,35,0.6) 75%, rgba(40,20,22,0) 100%);
  }
  .curriculum { position: absolute; left: 732px; top: 130px; width: 460px; }
  .curriculum-title {
    font-weight: 700; font-size: 33px; letter-spacing: 1px; text-transform: uppercase;
  }
  .topic-grid {
    display: grid; grid-template-columns: 243px 217px;
    grid-template-rows: 159px auto; margin-top: 24px;
  }
  .topic h3 { font-weight: 600; font-size: 18.5px; letter-spacing: 0.3px; }
  .topic ul { list-style: none; margin-top: 8px; }
  .topic li {
    font-size: 11.5px; line-height: 18.8px; color: var(--text-soft);
    padding-left: 7px; text-indent: -7px;
  }
  .topic li::before { content: "· "; }
</style>
</head>
<body>
  <div class="brand"><span class="brand-mark"></span>Dunecrest Motocross Club</div>

  <nav class="main-nav">
    <a href="#">CALENDER</a>
    <a href="#">ONLINE PAYMENT</a>
    <a href="#">RACE RESULT</a>
    <a href="#">ACADEMY</a>
    <a href="#">FACILITIES</a>
  </nav>

  <section class="hero-intro">
    <h1 class="hero-title">Take your racing<br>to the next level</h1>
    <p class="hero-tagline">Reserve Your Spot Today!</p>
    <p class="hero-copy">Lorem ipsum dolor sit amet, consetetur sadipscing elitr, sed diam nonumy eirmod tempor invidunt ut labore et dolore magna aliquyam erat, sed diam voluptua. At vero eos et accusam et justo duo dolores et ea rebum. Stet clita kasd gubergren, no sea takimata sanctus est Lorem ipsum dolor sit amet. Lorem ipsum dolor sit</p>
  </section>
  <a class="cta" href="#">Contact Us</a>

  <div class="rider-photo" role="img" aria-label="Photo of a motocross rider performing a jump trick on a dirt bike"></div>

  <section class="curriculum">
    <h2 class="curriculum-title">What we teach</h2>
    <div class="topic-grid">
      <div class="topic">
        <h3>The Basics</h3>
        <ul>
          <li>Braking, Shifting, Throttle Control</li>
          <li>Body Positioning (Standing, Sitting &amp; Weight Transfer)</li>
          <li>Proper Bike Setup</li>
        </ul>
      </div>
      <div class="topic">
        <h3>Cornering</h3>
        <ul>
          <li>Speed, Line Selection, Rutted &amp; Berm Corners</li>
          <li>Finding And Making New Lines</li>
          <li>Proper Entering And Exiting Of Cornering</li>
          <li>Body Positioning</li>
        </ul>
      </div>
      <div class="topic">
        <h3>Jumping</h3>
        <ul>
          <li>Double Jumping, Judging Launches And Landings</li>
          <li>Body Positioning</li>
          <li>Steep Jumps And Jumps With Kickers</li>
          <li>Rutted, Slick, Sand Jumping</li>
          <li>Line Selection And The "Seat Bounce Theory"</li>
        </ul>
      </div>
      <div class="topic">
        <h3>Start</h3>
        <ul>
          <li>Learning To Holeshot</li>
          <li>Mental Aspect, Gate Selection And Proper Positioning</li>
          <li>Real Gates At School Track</li>
        </ul>
      </div>
    </div>
  </section>
</body>
</html>
```